Transportation website

I need website for my company, its gonna be transportation and logistics website, information and address, contact form , service, about

```html
<!DOCTYPE html>
<html lang="en">
<head>
<meta charset="utf-8">
<title>Varro Freight</title>
<link href="https://fonts.googleapis.com/css2?family=Montserrat:wght@500;600;700&family=Open+Sans:wght@400;600;700&display=swap" rel="stylesheet">
<style>
:root{
  --orange:#f26a10;
  --orange-dark:#d85a08;
  --ink:#1c1c1c;
  --text:#555;
  --grey-bg:#f1f1f1;
  --footer:#1b1b1b;
  --white:#fff;
}
*{box-sizing:border-box;margin:0;padding:0}
html,body{width:1200px;height:4467px;overflow:hidden}
body{font-family:"Open Sans",Arial,sans-serif;color:var(--text);background:var(--white);position:relative}
h1,h2,h3,h4{font-family:"Montserrat",Arial,sans-serif}
section,header,footer{position:absolute;left:0;width:1200px}
.abs{position:absolute}

/* hero */
.hero{top:0;height:605px;background:linear-gradient(100deg,#1e2a38 0%,#2d4052 40%,#5a6470 70%,#8a6a4a 100%)}
.hero-photo{position:absolute;inset:0}
.hero-shade{position:absolute;inset:0;background:linear-gradient(90deg,rgba(10,15,25,.55),rgba(10,15,25,0) 70%)}
.brand{left:89px;top:26px;font:600 32px "Montserrat",sans-serif;color:var(--white)}
.nav{right:92px;top:38px;display:flex;gap:48px}
.nav a{color:var(--white);text-decoration:none;font-size:16px;font-weight:600}
.hero h1{left:89px;top:203px;font-size:56px;font-weight:700;color:var(--white);letter-spacing:1px}
.hero p{left:89px;top:282px;width:520px;font-size:17px;line-height:25px;color:#f0f0f0}
.btn{display:inline-block;background:var(--orange);color:var(--white);border-radius:30px;font:600 20px "Montserrat",sans-serif;text-align:center}
.hero .btn{left:92px;top:381px;width:215px;height:57px;line-height:57px}
.dots{left:548px;top:552px;display:flex;gap:14px}
.dots span{width:14px;height:14px;border-radius:50%;border:2px solid var(--white)}
.dots span:first-child{background:var(--white)}

/* welcome */
.welcome{top:605px;height:283px;text-align:center}
.welcome h2{margin-top:97px;font-size:34px;font-weight:700;color:var(--ink)}
.welcome p{width:914px;margin:26px auto 0;font-size:16.5px;line-height:30px}

/* features */
.features{top:888px;height:602px;background:var(--grey-bg)}
.feature-photo{left:0;top:0;width:563px;height:602px;background:linear-gradient(160deg,#9aa6ae 0%,#6d767d 40%,#b88a55 70%,#d4b070 100%)}
.feature{left:510px;width:640px;height:130px}
.feature .diamond{position:absolute;left:0;top:0;width:106px;height:106px}
.feature h3{position:absolute;left:133px;top:8px;font-size:26px;font-weight:600;color:var(--orange)}
.feature p{position:absolute;left:133px;top:52px;width:500px;font-size:16.5px;line-height:29px}

/* services */
.services{top:1490px;height:782px;background:linear-gradient(135deg,#e6701f 0%,#d96418 45%,#b85a20 75%,#8a4a2a 100%)}
.services h2{left:92px;top:136px;font-size:34px;font-weight:600;color:var(--white)}
.services .intro{left:92px;top:193px;width:320px;font-size:16.5px;line-height:29px;color:#fde6d5}
.card{width:320px;height:218px;background:#151515;color:var(--white)}
.card .diamond{position:absolute;left:22px;top:-52px;width:106px;height:106px}
.card h3{position:absolute;left:20px;top:80px;font-size:17px;font-weight:600;letter-spacing:.3px}
.card p{position:absolute;left:20px;top:110px;width:290px;font-size:15px;line-height:24px;color:#e6e6e6}
.card a{position:absolute;left:20px;top:170px;font-size:15px;font-weight:700;color:var(--white);text-decoration:none}

/* contact */
.contact{top:2272px;height:715px}
.contact h2{left:92px;top:132px;font-size:34px;font-weight:600;color:var(--ink)}
.contact .lead{left:92px;top:190px;width:300px;font-size:16px;line-height:25px}
.contact h4{left:92px;top:298px;font-size:20px;font-weight:600;color:var(--orange)}
.contact-item{left:92px;display:flex;gap:20px;font-size:15px;line-height:27px;color:#333}
.contact-item .ico{width:36px;height:36px;background:var(--orange);border-radius:4px;flex:none;display:flex;align-items:center;justify-content:center}
.ship-art{left:372px;top:200px;width:340px;height:313px;background:radial-gradient(ellipse at 55% 55%,#3d6db0 0%,#8fb0d6 45%,rgba(255,255,255,0) 72%)}
.form-box{left:673px;top:107px;width:435px;height:504px;background:var(--orange);padding:0 30px}
.form-box h3{margin-top:50px;font-size:26px;font-weight:600;color:var(--white)}
.field{border-bottom:1px solid rgba(255,255,255,.7);color:var(--white);font-size:15px;padding-bottom:10px;margin-top:24px}
.field.msg{margin-top:94px}
.submit{margin-top:33px;width:140px;height:42px;line-height:38px;border:2px solid var(--white);border-radius:22px;font:600 16px "Montserrat",sans-serif;color:var(--white);text-align:center}

/* blog */
.blog{top:2987px;height:661px;background:var(--grey-bg)}
.blog h2{width:100%;text-align:center;top:100px;font-size:34px;font-weight:600;color:var(--ink)}
.post{top:173px;width:325px;height:378px;background:var(--white);box-shadow:4px 6px 10px rgba(0,0,0,.2)}
.post .thumb{height:175px}
.post .date{position:absolute;left:14px;top:14px;width:62px;height:68px;background:var(--orange);color:var(--white);text-align:center;font:700 16px/22px "Montserrat",sans-serif;padding-top:12px}
.post h3{margin:20px 14px 0;font-size:17px;line-height:24px;font-weight:600;color:var(--ink)}
.post p{margin:12px 14px 0;font-size:14.5px;line-height:25px}
.post a{display:block;margin:14px 14px 0;font-size:15px;font-weight:700;color:var(--orange);text-decoration:none}

/* partners */
.partners{top:3648px;height:268px;display:flex;align-items:center;justify-content:space-between;padding:0 92px}
.partner{display:flex;align-items:center;gap:10px;font:600 26px "Montserrat",sans-serif;color:#555}
.partner i{width:22px;height:22px;background:#555;display:block}

/* newsletter */
.newsletter{top:3916px;height:158px;background:var(--orange)}
.newsletter h4{left:182px;top:64px;font-size:21px;font-weight:500;color:var(--white);letter-spacing:.5px}
.newsletter .input{left:524px;top:54px;width:444px;height:50px;background:var(--white);font-size:15px;line-height:50px;padding-left:16px;color:#444}
.newsletter .send{left:968px;top:54px;width:50px;height:50px;background:#151515;display:flex;align-items:center;justify-content:center}

/* footer */
.footer{top:4074px;height:393px;background:var(--footer);color:#ddd}
.col h4{font-size:17px;font-weight:600;color:var(--white);margin-top:52px}
.col ul{list-style:none;margin-top:20px}
.col li{font-size:14px;line-height:31px}
.social{display:flex;gap:14px;margin-top:14px}
.social span{width:14px;height:14px;border-radius:50%;background:var(--white)}
.copy{width:100%;top:4353px;text-align:center;font-size:14px;color:#ccc;position:absolute}
</style>
</head>
<body>

<header class="hero">
  <div class="hero-photo" role="img" aria-label="Worker in hard hat and safety vest with clipboard in a container yard"></div>
  <div class="hero-shade"></div>
  <div class="abs brand">Varro Freight</div>
  <nav class="abs nav"><a href="#">Home</a><a href="#">About Us</a><a href="#">Services</a><a href="#">Blog</a><a href="#">Contact Us</a></nav>
  <h1 class="abs">VARRO FREIGHT</h1>
  <p class="abs">Lorem ipsum dolor sit amet, consectetur adipiscing elit, sed do eiusmod tempor incididunt ut labore et dolore magna</p>
  <a class="abs btn" href="#">Contact Us</a>
  <div class="abs dots"><span></span><span></span><span></span><span></span></div>
</header>

<section class="welcome">
  <h2>Welcome To Varro Freight</h2>
  <p>Lorem ipsum dolor sit amet, consectetur adipiscing elit, sed do eiusmod tempor incididunt ut labore et dolore magna aliqua. Ut enim ad minim veniam, quis nostrud exercitation ullamco laboris nisi ut aliquip ex ea commodo consequat. Duis aute irure dolor in reprehenderit in voluptate velit esse cillum dolore eu fugiat nulla pariatur.</p>
</section>

<section class="features">
  <div class="abs feature-photo" role="img" aria-label="Forklift carrying stacked cardboard boxes in a warehouse"></div>
  <div class="abs feature" style="top:59px">
    <svg class="diamond" viewBox="0 0 106 106"><rect x="18" y="18" width="70" height="70" transform="rotate(45 53 53)" fill="var(--orange)"/><circle cx="53" cy="45" r="8" fill="#fff"/><path d="M38 68c2-10 8-14 15-14s13 4 15 14z" fill="#fff"/></svg>
    <h3>Lorem ipsum</h3>
    <p>Lorem ipsum dolor sit amet, consectetur adipiscing elit, sed do eiusmod tempor incididunt ut labore et dolore magna</p>
  </div>
  <div class="abs feature" style="top:235px">
    <svg class="diamond" viewBox="0 0 106 106"><rect x="18" y="18" width="70" height="70" transform="rotate(45 53 53)" fill="var(--orange)"/><circle cx="53" cy="53" r="14" fill="none" stroke="#fff" stroke-width="6" stroke-dasharray="6 4"/><circle cx="53" cy="53" r="5" fill="#fff"/></svg>
    <h3>Lorem ipsum</h3>
    <p>Lorem ipsum dolor sit amet, consectetur adipiscing elit, sed do eiusmod tempor incididunt ut labore et dolore magna</p>
  </div>
  <div class="abs feature" style="top:410px">
    <svg class="diamond" viewBox="0 0 106 106"><rect x="18" y="18" width="70" height="70" transform="rotate(45 53 53)" fill="var(--orange)"/><circle cx="53" cy="53" r="15" fill="none" stroke="#fff" stroke-width="3"/><path d="M53 44v10l6 4" stroke="#fff" stroke-width="3" fill="none"/></svg>
    <h3>Lorem ipsum</h3>
    <p>Lorem ipsum dolor sit amet, consectetur adipiscing elit, sed do eiusmod tempor incididunt ut labore et dolore magna</p>
  </div>
</section>

<section class="services" role="img" aria-label="Aerial view of a container port tinted orange">
  <h2 class="abs">Our Services</h2>
  <p class="abs intro">Lorem ipsum dolor sit amet, consectetur adipiscing elit, sed do eiusmod tempor incididunt ut labore et dolore magna aliqua.</p>

  <div class="abs card" style="left:441px;top:142px">
    <svg class="diamond" viewBox="0 0 106 106"><rect x="18" y="18" width="70" height="70" transform="rotate(45 53 53)" fill="#151515" stroke="#fff" stroke-width="3"/><path d="M40 60l26-16M50 48l-6-8 4-1 10 6M56 58l4 10-3 1-8-8" stroke="#fff" stroke-width="3" fill="none"/></svg>
    <h3>ALL MODE TRANSPORTATION</h3>
    <p>Lorem ipsum dolor sit amet, consectetur adipiscing elit, sed do eiusmod tempor</p>
    <a href="#">Read More »</a>
  </div>
  <div class="abs card" style="left:789px;top:142px">
    <svg class="diamond" viewBox="0 0 106 106"><rect x="18" y="18" width="70" height="70" transform="rotate(45 53 53)" fill="#151515" stroke="#fff" stroke-width="3"/><rect x="42" y="46" width="22" height="16" fill="#fff"/><path d="M64 50h6l4 6v6H64" fill="#fff"/><path d="M44 40h14" stroke="#fff" stroke-width="3"/></svg>
    <h3>REVERSE LOGISTICS</h3>
    <p>Lorem ipsum dolor sit amet, consectetur adipiscing elit, sed do eiusmod tempor</p>
    <a href="#">Read More »</a>
  </div>
  <div class="abs card" style="left:92px;top:481px">
    <svg class="diamond" viewBox="0 0 106 106"><rect x="18" y="18" width="70" height="70" transform="rotate(45 53 53)" fill="#151515" stroke="#fff" stroke-width="3"/><rect x="40" y="42" width="26" height="20" fill="none" stroke="#fff" stroke-width="3"/><path d="M36 66h34" stroke="#fff" stroke-width="3"/></svg>
    <h3>TECHNOLOGY</h3>
    <p>Lorem ipsum dolor sit amet, consectetur adipiscing elit, sed do eiusmod tempor</p>
    <a href="#">Read More »</a>
  </div>
  <div class="abs card" style="left:441px;top:481px">
    <svg class="diamond" viewBox="0 0 106 106"><rect x="18" y="18" width="70" height="70" transform="rotate(45 53 53)" fill="#151515" stroke="#fff" stroke-width="3"/><rect x="44" y="40" width="12" height="12" fill="#fff"/><rect x="52" y="54" width="14" height="12" fill="#fff"/><path d="M40 38v28h28" stroke="#fff" stroke-width="3" fill="none"/></svg>
    <h3>LOGISTICS CONSULTING</h3>
    <p>Lorem ipsum dolor sit amet, consectetur adipiscing elit, sed do eiusmod tempor</p>
    <a href="#">Read More »</a>
  </div>
  <div class="abs card" style="left:789px;top:481px">
    <svg class="diamond" viewBox="0 0 106 106"><rect x="18" y="18" width="70" height="70" transform="rotate(45 53 53)" fill="#151515" stroke="#fff" stroke-width="3"/><circle cx="53" cy="47" r="8" fill="none" stroke="#fff" stroke-width="3"/><path d="M40 68c2-8 7-11 13-11s11 3 13 11" stroke="#fff" stroke-width="3" fill="none"/></svg>
    <h3>CUSTOMER SERVICES</h3>
    <p>Lorem ipsum dolor sit amet, consectetur adipiscing elit, sed do eiusmod tempor</p>
    <a href="#">Read More »</a>
  </div>
</section>

<section class="contact">
  <h2 class="abs">Contact Us</h2>
  <p class="abs lead">Sed ut perspiciatis unde omnis iste natus error sit voluptatem accusantium doloremque laudantium.</p>
  <h4 class="abs">ADDRESS</h4>
  <div class="abs contact-item" style="top:366px">
    <span class="ico"><svg width="18" height="22" viewBox="0 0 18 22"><path d="M9 1a7 7 0 0 0-7 7c0 5 7 13 7 13s7-8 7-13a7 7 0 0 0-7-7z" fill="#fff"/><circle cx="9" cy="8" r="2.5" fill="var(--orange)"/></svg></span>
    <span>48 Harbor Line Road,<br>Suite 9, Eastport,<br>USA</span>
  </div>
  <div class="abs contact-item" style="top:470px;align-items:center">
    <span class="ico"><svg width="20" height="20" viewBox="0 0 20 20"><path d="M4 2l4 4-2 3c1 2 3 4 5 5l3-2 4 4-3 3C8 19 1 12 1 5z" fill="#fff"/></svg></span>
    <span>+415 555 0148</span>
  </div>
  <div class="abs contact-item" style="top:542px;align-items:center">
    <span class="ico"><svg width="20" height="16" viewBox="0 0 20 16"><rect x="1" y="1" width="18" height="14" fill="#fff"/><path d="M1 1l9 8 9-8" stroke="var(--orange)" stroke-width="2" fill="none"/></svg></span>
    <span>info@varrofreight.com</span>
  </div>
  <div class="abs ship-art" role="img" aria-label="Cargo ship, globe and plane illustrating worldwide shipping"></div>
  <div class="abs form-box">
    <h3>Contact Form</h3>
    <div class="field" style="margin-top:40px">Name</div>
    <div class="field">Email</div>
    <div class="field">Phone No</div>
    <div class="field msg">Message</div>
    <div class="submit">SUBMIT</div>
  </div>
</section>

<section class="blog">
  <h2 class="abs">Blog</h2>
  <article class="abs post" style="left:92px">
    <div class="thumb" role="img" aria-label="Worker driving a forklift between warehouse shelves" style="background:linear-gradient(135deg,#6a6258,#c7a070 60%,#e0c79a)"></div>
    <div class="date">FEB<br>15</div>
    <h3>SED UT PERSPICIATIS UNDE OMNIS ISTE NATUS</h3>
    <p>Lorem ipsum dolor sit amet, consectetur adipiscing elit, sed do eiusmod tempor incididunt ut labore et dolore</p>
    <a href="#">Read More »</a>
  </article>
  <article class="abs post" style="left:441px">
    <div class="thumb" role="img" aria-label="Aerial view of a container ship at sea" style="background:linear-gradient(135deg,#0f4e7a,#2a7fb0 55%,#4a9ccc)"></div>
    <div class="date">FEB<br>15</div>
    <h3>SED UT PERSPICIATIS UNDE OMNIS ISTE NATUS</h3>
    <p>Lorem ipsum dolor sit amet, consectetur adipiscing elit, sed do eiusmod tempor incididunt ut labore et dolore</p>
    <a href="#">Read More »</a>
  </article>
  <article class="abs post" style="left:783px">
    <div class="thumb" role="img" aria-label="Tall warehouse racks with stored goods" style="background:linear-gradient(135deg,#5a4a48,#a06050 50%,#d0a890)"></div>
    <div class="date">FEB<br>15</div>
    <h3>SED UT PERSPICIATIS UNDE OMNIS ISTE NATUS</h3>
    <p>Lorem ipsum dolor sit amet, consectetur adipiscing elit, sed do eiusmod tempor incididunt ut labore et dolore</p>
    <a href="#">Read More »</a>
  </article>
</section>

<section class="partners">
  <div class="partner">Northwind</div>
  <div class="partner"><i></i>Baymark</div>
  <div class="partner">Ketterly</div>
  <div class="partner">Orchid Co</div>
  <div class="partner"><i style="border-radius:50%"></i>Lumenfold</div>
</section>

<section class="newsletter">
  <h4 class="abs">SIGN UP OUR NEWSLETTER</h4>
  <div class="abs input">Email Address</div>
  <div class="abs send"><svg width="22" height="22" viewBox="0 0 22 22"><path d="M2 10L20 2l-6 18-3-8z" fill="none" stroke="#fff" stroke-width="2" stroke-linejoin="round"/><path d="M11 12l9-10" stroke="#fff" stroke-width="2"/></svg></div>
</section>

<footer class="footer">
  <div class="abs col" style="left:92px"><h4>COMPANY</h4><ul><li>Home</li><li>About Us</li><li>Services</li><li>Blog</li><li>Contact Us</li></ul></div>
  <div class="abs col" style="left:369px"><h4>CONTACT</h4><ul><li>Corporate Office</li><li>(816) 555-0192</li><li>info@varrofreight.com</li></ul></div>
  <div class="abs col" style="left:649px"><h4>LEGAL</h4><ul><li>Privacy Policy</li><li>Faq</li><li>Sitemap</li><li>Contact Us</li></ul></div>
  <div class="abs col" style="left:992px"><h4>MY ACCOUNT</h4><ul><li>Log In</li><li>Sign Up</li></ul><h4 style="margin-top:22px">FOLLOW US</h4><div class="social"><span></span><span></span><span></span><span></span></div></div>
</footer>
<div class="copy">© 2019 The Company name. All rights Reserved Privacy Policy | Terms Of Use</div>

</body>
</html>
```